Killer business card for bowling event and marketing company

Rolling 'T' Ventures is a sports marketing company that specializes in unique bowling events that provide return on investment for sponsors and memorable experiences for participants and spectators. We need a new business card that simultaneously communicates professionalism and fun. Our preferred colors are black and re

Target Market(s)

Executives in the marketing and sponsorship departments of companies, tourism executives, bowling center owners, and people who love to bowl.

Industry/Entity Type

Business

Contact Information for Business Card

Neil T Farrow
Rolling 'T' Ventures
PO Box 47
Millbrook, Ohio USA 00000
Email: neilt@rollingtventures.example
Mobile: 1-555-318-4762

Requirements
Must have
• Our preferred colors are black and red.
Nice to have
• I am considering the use of the attached image for the back of the card.

```html
<!DOCTYPE html>
<html lang="en">
<head>
<meta charset="utf-8">
<title>Rolling 'T' Ventures — Business Card</title>
<link href="https://fonts.googleapis.com/css2?family=Exo+2:wght@700;800&family=Open+Sans:wght@400;600&display=swap" rel="stylesheet">
<style>
  :root {
    --backdrop: #1c1c1e;
    --card-white: #ffffff;
    --brand-red: #b81c24;
    --ink: #1a1a1a;
    --ink-soft: #3c3c3c;
    --photo-dark: #0c0807;
    --photo-red: #8e2a1c;
    --photo-tan: #c9a46a;
  }
  * { margin: 0; padding: 0; box-sizing: border-box; }
  html, body {
    width: 1200px; height: 1000px; overflow: hidden;
    background: var(--backdrop);
  }
  .canvas { position: relative; width: 1200px; height: 1000px; }

  .card {
    position: absolute;
    width: 560px; height: 320px;
    border-radius: 26px;
    overflow: hidden;
  }

  /* Back of card */
  .card-back { left: 90px; top: 130px; background: var(--photo-dark); }
  .card-back .photo {
    position: absolute; inset: 0;
    background:
      radial-gradient(ellipse at 55% 75%, rgba(201,164,106,.55) 0%, rgba(142,42,28,.55) 35%, transparent 70%),
      linear-gradient(160deg, #2a2a2e 0%, var(--photo-dark) 35%, var(--photo-red) 70%, var(--photo-dark) 100%);
  }
  .card-back .brand {
    position: absolute; left: 0; right: 0; top: 92px;
    display: flex; flex-direction: column; align-items: center; gap: 14px;
  }
  .brand-square {
    width: 58px; height: 58px;
    background: var(--brand-red);
    border-radius: 8px;
    flex: none;
  }
  .card-back .brand-name {
    font-family: "Exo 2", sans-serif; font-weight: 800;
    font-size: 32px; line-height: 1; color: var(--card-white);
    text-transform: uppercase; letter-spacing: .5px;
    white-space: nowrap; text-align: center;
  }

  /* Front of card */
  .card-front { left: 550px; top: 520px; background: var(--card-white); }
  .card-front .base-band {
    position: absolute; left: 0; right: 0; bottom: 0; height: 20px;
    background: var(--brand-red);
  }
  .card-front .brand {
    position: absolute; right: 40px; top: 34px;
    display: flex; align-items: center; gap: 12px;
  }
  .card-front .brand-square { width: 44px; height: 44px; border-radius: 6px; }
  .card-front .brand-name {
    font-family: "Exo 2", sans-serif; font-weight: 800;
    font-size: 24px; color: var(--ink); text-transform: uppercase;
    white-space: nowrap;
  }

  .holder { position: absolute; left: 40px; top: 128px; }
  .holder-name {
    font-family: "Exo 2", sans-serif; font-weight: 800;
    font-size: 30px; color: var(--brand-red);
    letter-spacing: 1px; text-transform: uppercase; white-space: nowrap;
  }
  .holder-company {
    font-family: "Open Sans", sans-serif; font-size: 15px;
    color: var(--ink-soft); margin-top: 2px;
  }
  .rule {
    position: absolute; left: 210px; right: 34px; top: 170px;
    height: 2px; background: var(--brand-red);
  }
  .address {
    position: absolute; right: 40px; top: 184px;
    font-family: "Open Sans", sans-serif; font-size: 14px; font-style: normal;
    color: var(--ink-soft); text-align: right; line-height: 1.35;
  }
  .contacts {
    position: absolute; left: 40px; top: 214px;
    list-style: none;
    font-family: "Open Sans", sans-serif; font-size: 14px; color: var(--ink-soft);
  }
  .contacts li { display: flex; align-items: center; gap: 10px; height: 22px; }
  .contacts svg { width: 12px; height: 12px; fill: var(--brand-red); flex: none; }
  .contacts .accent { color: var(--brand-red); }
</style>
</head>
<body>
<main class="canvas">

  <section class="card card-back" aria-label="Card back">
    <div class="photo" role="img" aria-label="Photograph looking down a bowling lane toward the pins, in dark red and tan tones"></div>
    <div class="brand">
      <div class="brand-square"></div>
      <div class="brand-name">Rolling 'T' Ventures</div>
    </div>
  </section>

  <section class="card card-front" aria-label="Card front">
    <div class="brand">
      <div class="brand-square"></div>
      <div class="brand-name">Rolling 'T' Ventures</div>
    </div>

    <div class="holder">
      <h1 class="holder-name">Neil T Farrow</h1>
      <p class="holder-company">Rolling 'T' Ventures</p>
    </div>
    <div class="rule"></div>

    <address class="address">
      PO Box 47, Millbrook<br>Ohio USA 00000
    </address>

    <ul class="contacts">
      <li>
        <svg viewBox="0 0 24 24"><path d="M6.6 10.8a15.1 15.1 0 0 0 6.6 6.6l2.2-2.2c.3-.3.7-.4 1-.2 1.1.4 2.3.6 3.6.6.6 0 1 .4 1 1V20c0 .6-.4 1-1 1A17 17 0 0 1 3 4c0-.6.4-1 1-1h3.5c.6 0 1 .4 1 1 0 1.3.2 2.5.6 3.6.1.3 0 .7-.2 1z"/></svg>
        1-555-318-4762
      </li>
      <li>
        <svg viewBox="0 0 24 24"><path d="M2 5h20v14H2z"/><path d="M2 6l10 7 10-7v-1H2z" fill="#fff"/></svg>
        neilt@rollingtventures.example
      </li>
      <li>
        <svg viewBox="0 0 24 24"><circle cx="12" cy="12" r="10"/><path d="M2 12h20M12 2c3 3 3 17 0 20M12 2c-3 3-3 17 0 20" stroke="#fff" stroke-width="1.5" fill="none"/></svg>
        <span>www.<span class="accent">rollingtventures</span>.example</span>
      </li>
    </ul>

    <div class="base-band"></div>
  </section>

</main>
</body>
</html>
```